Project, Programme and Portfolio Management Consultant needs a business card

I have recently had someone create a brand guide for me and I wish to have new business cards that incorporate the new brand. I am an independent management consultant working with businesses to improve their ability to deliver their business strategy through selecting the right project, the right people and doing it in the right way. Whilst I am currently working on my own, I am hoping to start to build win business where I need to bring in a team and this branding activity is the start of that process.

Target Market(s)

Medium to large businesses, government departments and defence

Contact Information for Business Card

Name
job title
business name
mobile
email
website
linkedIn profile

Font styles to use
Other font styles liked:
• roboto light

Colors

Designer to choose colors to be used in the design.

Requirements
Must have
• Must use my logo and brand colours (see attached brand guide)

```html
<!DOCTYPE html>
<html lang="en">
<head>
<meta charset="utf-8">
<title>Kelvard Business Card</title>
<link rel="stylesheet" href="https://fonts.googleapis.com/css2?family=Roboto:wght@400;500&display=swap">
<style>
  :root {
    --stage: #d6d6d6;
    --paper: #ffffff;
    --navy: #1f3565;
    --navy-deep: #1e3866;
    --ink: #1a1f36;
    --teal: #16a99c;
    --gold: #e3a92a;
  }
  * { margin: 0; padding: 0; box-sizing: border-box; }
  html, body { width: 1000px; height: 1200px; overflow: hidden; }
  body {
    background: var(--stage);
    font-family: "Roboto", Arial, sans-serif;
    position: relative;
  }
  .card {
    position: absolute;
    box-shadow: 6px 8px 18px rgba(0,0,0,0.35);
  }
  .card-front {
    left: 111px; top: 120px; width: 777px; height: 446px;
    background: var(--paper);
  }
  .brand-name {
    position: absolute;
    left: 102px; top: 312px; width: 207px;
    text-align: center;
    font-size: 40px; font-weight: 400; letter-spacing: 3px;
    color: var(--ink);
    line-height: 1;
  }
  .divider {
    position: absolute;
    left: 356px; top: 100px; width: 2px; height: 251px;
    background: var(--teal);
  }
  .details {
    position: absolute;
    left: 405px; top: 97px;
    color: var(--ink);
  }
  .person-name { font-size: 23px; font-weight: 500; color: var(--navy); line-height: 30px; }
  .person-role { font-size: 18px; line-height: 24px; }
  .business-name { margin-top: 12px; font-size: 19px; font-weight: 500; color: var(--navy); line-height: 24px; }
  .address { font-size: 19px; line-height: 26px; }
  .contacts { margin-top: 11px; list-style: none; }
  .contacts li {
    display: flex; align-items: center;
    font-size: 19px; line-height: 26.5px;
  }
  .contacts svg { width: 17px; height: 17px; margin-right: 10px; fill: var(--navy); flex: none; }
  .card-back {
    left: 109px; top: 633px; width: 782px; height: 446px;
    background: var(--navy-deep);
  }
  .back-brand {
    position: absolute;
    left: 580px; top: 282px;
    font-size: 22px; font-weight: 500; letter-spacing: 2px;
    color: var(--gold);
  }
</style>
</head>
<body>
  <section class="card card-front">
    <div class="brand-name">KELVARD</div>
    <div class="divider"></div>
    <div class="details">
      <h1 class="person-name">ADRIAN HOLLOWAY</h1>
      <p class="person-role">Owner</p>
      <h2 class="business-name">BUSINESS NAME</h2>
      <p class="address">2187 Larkfield Avenue, Brennmoor<br>NC 2, United States</p>
      <ul class="contacts">
        <li><svg viewBox="0 0 24 24"><path d="M6.6 10.8a15.2 15.2 0 0 0 6.6 6.6l2.2-2.2a1 1 0 0 1 1-.25 11.4 11.4 0 0 0 3.6.57 1 1 0 0 1 1 1V20a1 1 0 0 1-1 1A17 17 0 0 1 3 4a1 1 0 0 1 1-1h3.5a1 1 0 0 1 1 1c0 1.25.2 2.45.57 3.57a1 1 0 0 1-.25 1z"/></svg>000-000-000-000</li>
        <li><svg viewBox="0 0 24 24"><path d="M2 5h20v14H2z M3.5 6.5 12 13l8.5-6.5" fill="var(--navy)"/><path d="M3 6l9 7 9-7" fill="none" stroke="#fff" stroke-width="1.6"/></svg>hello@kelvardconsulting.com</li>
        <li><svg viewBox="0 0 24 24"><circle cx="12" cy="12" r="9" fill="none" stroke="var(--navy)" stroke-width="2"/><ellipse cx="12" cy="12" rx="4" ry="9" fill="none" stroke="var(--navy)" stroke-width="1.6"/><path d="M3 12h18M5 7.5h14M5 16.5h14" stroke="var(--navy)" stroke-width="1.4"/></svg>www.kelvardconsulting.com</li>
        <li><svg viewBox="0 0 24 24"><circle cx="12" cy="12" r="10"/></svg>/kelvardconsulting</li>
      </ul>
    </div>
  </section>

  <section class="card card-back" role="img" aria-label="Navy card back with a faint repeating brand pattern">
    <div class="back-brand">KELVARD</div>
  </section>
</body>
</html>
```